“The Future” Spring Fair Poster

We are putting together a school and community fair. We need a poster designed to advertise the event and give some important information to would be attendees. We’d like the poster graphics to evoke a minimalistic and futuristic aesthetic, be bold, yet fun! We will printing the posters, so we will need for them to be at high resolution and ready to send to print.

Target Market(s)

Students, Parents, and Community members

Industry/Entity Type

School

Font styles to use
Sans Serif

Colors
33a6d7
fabb78
9d9d9d
ffffff
1b1b1b
33b8a4

Requirements
Must have
• The Future
• Birch & Harbor Spring Fair 2018
• Friday, May 18th
• 5:00-9:00pm
• Tickets Will Be Available at Select Pick up & Drop Off Times
• Come Enjoy a Futuristic Evening of Food, Music, Entertainment, & Fun!
Nice to have
• We’d love to see a bold and graphic poster with a futuristic feel!
• See the sample image below from previous event poster and additional images for mood and inspiration. Would love to see metallics (silver or metallic colors)

```html
<!DOCTYPE html>
<html lang="en">
<head>
<meta charset="utf-8">
<title>The Future – Birch &amp; Harbor Spring Fair 2018</title>
<link href="https://fonts.googleapis.com/css2?family=Orbitron:wght@500;700;900&display=swap" rel="stylesheet">
<style>
  :root {
    --space-deep: #2a0f5e;
    --space-violet: #5b22a6;
    --space-magenta: #8a34d8;
    --brand-blue: #33a6d7;
    --brand-teal: #33b8a4;
    --brand-peach: #fabb78;
    --silver: #ffffff;
    --silver-shade: #9d9d9d;
    --ink-dark: #1b1b1b;
    --triangle-dark: #26124f;
    --floor-top: #b27cff;
    --floor-bottom: #6a2bd4;
  }
  * { margin: 0; padding: 0; box-sizing: border-box; }
  html, body { width: 800px; height: 1200px; overflow: hidden; background: var(--space-deep); }
  .poster {
    position: relative; width: 800px; height: 1200px; overflow: hidden;
    color: var(--silver);
    font-family: "Orbitron", sans-serif; text-transform: uppercase;
    background:
      radial-gradient(circle 90px at 644px 944px, rgba(255,255,255,.55), transparent 70%),
      radial-gradient(ellipse 260px 140px at 300px 330px, rgba(220,190,255,.35), transparent 70%),
      radial-gradient(ellipse 420px 200px at 420px 860px, rgba(51,166,215,.45), transparent 70%),
      radial-gradient(ellipse 300px 260px at 700px 560px, rgba(210,110,255,.45), transparent 70%),
      radial-gradient(ellipse 360px 220px at 60px 700px, rgba(51,184,164,.12), transparent 70%),
      linear-gradient(180deg, #3a1678 0%, #5b22a6 38%, #7a2fd0 62%, #4a23c8 78%, #6a2bd4 100%);
  }
  .backdrop { position: absolute; inset: 0; }
  .floor { position: absolute; left: 0; top: 886px; width: 800px; height: 314px; }

  .headline { position: absolute; top: 30px; left: 0; width: 800px; text-align: center; }
  .headline p { text-shadow: 0 0 6px rgba(255,255,255,.45); }
  .invite { font-size: 14px; font-weight: 700; letter-spacing: 9px; }
  .evening { margin-top: 14px; font-size: 11px; font-weight: 700; letter-spacing: 4px; }
  .evening strong { font-size: 25px; font-weight: 700; letter-spacing: 0; }
  .offerings { margin-top: 6px; font-size: 24px; font-weight: 700; letter-spacing: 0; }

  .title-block { position: absolute; inset: 0; }
  .title-block span {
    position: absolute; white-space: nowrap;
    transform: translate(-50%, -50%) rotate(-28deg);
    color: #ececf2;
    text-shadow: 1px 2px 0 var(--silver-shade), 3px 5px 10px rgba(27,27,27,.6);
  }
  .title-main  { left: 420px; top: 383px; font-size: 58px; font-weight: 900; }
  .title-name  { left: 372px; top: 492px; font-size: 34px; font-weight: 500; }
  .title-fair  { left: 391px; top: 583px; font-size: 34px; font-weight: 500; }
  .title-year  { left: 455px; top: 617px; font-size: 52px; font-weight: 900; }
  .event-day   { left: 441px; top: 739px; font-size: 27px; font-weight: 700; }
  .event-time  { left: 464px; top: 811px; font-size: 20px; font-weight: 700; }

  .tickets {
    position: absolute; left: 0; top: 1128px; width: 800px; text-align: center;
    font-size: 14px; font-weight: 700; letter-spacing: 7px; line-height: 30px;
    text-shadow: 0 0 6px rgba(255,255,255,.4);
  }
</style>
</head>
<body>
<main class="poster">
  <svg class="backdrop" viewBox="0 0 800 1200" width="800" height="1200" aria-hidden="true">
    <polygon class="triangle-back" points="133,316 678,355 455,766" fill="#3a1d72" opacity=".55"/>
    <polygon class="triangle-front" points="94,533 722,366 566,944" fill="var(--triangle-dark)" opacity=".6"/>
  </svg>

  <svg class="floor" viewBox="0 0 800 314" width="800" height="314" role="img" aria-label="Glowing purple perspective grid floor stretching toward the horizon">
    <defs>
      <linearGradient id="floor-fill" x1="0" y1="0" x2="0" y2="1">
        <stop offset="0" stop-color="var(--floor-top)" stop-opacity=".85"/>
        <stop offset="1" stop-color="var(--floor-bottom)" stop-opacity=".9"/>
      </linearGradient>
    </defs>
    <polygon points="70,0 730,0 800,314 0,314" fill="url(#floor-fill)"/>
  </svg>

  <header class="headline">
    <p class="invite">Come Enjoy</p>
    <p class="evening">a <strong>Futuristic Evening</strong> of</p>
    <p class="offerings">Food, Music, Entertainment, &amp; Fun!</p>
  </header>

  <section class="title-block">
    <span class="title-main">The Future</span>
    <span class="title-name">Birch &amp; Harbor</span>
    <span class="title-fair">Spring Fair</span>
    <span class="title-year">2018</span>
    <span class="event-day">Friday, May 18th</span>
    <span class="event-time">5:00-9:00pm</span>
  </section>

  <footer class="tickets">
    <p>Tickets will be available</p>
    <p>at select pick up + drop off times</p>
  </footer>
</main>
</body>
</html>
```